TAILWIND FIELDS Pet Resorts Outdoor Signage

4 x 8 outdoor signage design for our two locations

Target Market(s)

Existing and New Customers

Industry/Entity Type

Pet Care

Font styles to use
Sans Serif

Colors

Designer to choose colors to be used in the design.

```html
<!DOCTYPE html>
<html lang="en">
<head>
<meta charset="utf-8">
<title>TAILWIND FIELDS Pet Resorts – Outdoor Signage</title>
<link rel="stylesheet" href="https://fonts.googleapis.com/css2?family=Open+Sans:wght@300;400;600;700;800&display=swap">
<style>
  :root {
    --teal: #1aa3a3;
    --charcoal: #48484a;
    --white: #ffffff;
    --paper-top: #eceef0;
    --backdrop: #dcdcdc;
  }
  * { box-sizing: border-box; margin: 0; padding: 0; }
  html, body { width: 1200px; height: 1200px; overflow: hidden; }
  body {
    background: var(--backdrop);
    font-family: "Open Sans", Arial, sans-serif;
    position: relative;
  }
  .sign {
    position: absolute;
    top: 187px;
    width: 413px;
    height: 824px;
    background: linear-gradient(180deg, var(--paper-top) 0%, var(--white) 40%);
    overflow: hidden;
  }
  .sign--resort { left: 140px; }
  .sign--campus { left: 647px; }
  .sign__shapes { position: absolute; inset: 0; width: 100%; height: 100%; }
  .sign__shapes .band-dark { fill: var(--charcoal); }
  .sign__shapes .band-teal { fill: var(--teal); }

  .brand-name {
    position: absolute;
    left: 0; right: 0;
    top: 110px;
    text-align: center;
    color: var(--charcoal);
    font-weight: 800;
    font-size: 58px;
    line-height: 1.02;
    letter-spacing: 0.5px;
  }

  .headline {
    position: absolute;
    left: 0; right: 0;
    text-align: center;
    color: var(--white);
    font-weight: 800;
    text-transform: uppercase;
  }
  .headline--breed { top: 430px; font-size: 54px; line-height: 1.02; }
  .headline--campus { top: 448px; font-size: 43px; line-height: 1.0; }

  .rule {
    position: absolute;
    left: 52px; width: 310px; top: 594px; height: 2px;
    background: linear-gradient(90deg, transparent, rgba(255,255,255,.85) 20%, rgba(255,255,255,.85) 80%, transparent);
  }
  .tagline {
    position: absolute;
    left: 0; right: 0; top: 612px;
    text-align: center;
    color: var(--white);
    line-height: 1.05;
  }
  .tagline__lead { display: block; font-weight: 300; font-size: 31px; letter-spacing: 0.5px; }
  .tagline__main { display: block; font-weight: 800; font-size: 44px; }

  .services {
    position: absolute;
    left: 0; right: 0; top: 600px;
    height: 95px;
  }
  .service {
    position: absolute;
    top: 0;
    width: 110px;
    margin-left: -55px;
    text-align: center;
  }
  .service--boarding { left: 77px; }
  .service--daycare { left: 204px; top: 2px; }
  .service--training { left: 330px; top: 2px; }
  .service__icon {
    display: block;
    width: 72px; height: 60px;
    margin: 0 auto;
    background: var(--white);
    border-radius: 46% 54% 42% 58% / 55% 50% 50% 45%;
  }
  .service__label {
    display: block;
    margin-top: 14px;
    color: var(--white);
    font-weight: 700;
    font-size: 17px;
  }
  .services__divider {
    position: absolute;
    top: 21px; width: 2px; height: 60px;
    background: var(--white);
  }
  .services__divider--one { left: 141px; }
  .services__divider--two { left: 266px; }

  .contact {
    position: absolute;
    left: 0; right: 0; top: 746px;
    text-align: center;
    color: var(--white);
  }
  .contact__phone {
    display: flex; align-items: center; justify-content: center; gap: 8px;
    font-weight: 700; font-size: 31px; line-height: 1.2;
  }
  .contact__web {
    display: flex; align-items: center; justify-content: center; gap: 8px;
    font-weight: 400; font-size: 19px; line-height: 1.3;
  }
  .contact__web strong { font-weight: 700; }
  .contact svg { flex: none; }
</style>
</head>
<body>

  <!-- Sign one: resort services -->
  <section class="sign sign--resort">
    <svg class="sign__shapes" viewBox="0 0 665 1327" preserveAspectRatio="none" aria-hidden="true">
      <path class="band-dark" d="M0,525 Q330,760 665,525 L665,610 Q380,800 0,540 Z"/>
      <path class="band-teal" d="M0,552 Q380,812 665,620 L665,1183 L0,1183 Z"/>
      <rect class="band-dark" x="0" y="1191" width="665" height="136"/>
    </svg>

    <h1 class="brand-name">TAILWIND<br>FIELDS</h1>

    <h2 class="headline headline--breed">All Breed<br>Friendly</h2>

    <div class="services">
      <div class="service service--boarding">
        <span class="service__icon" role="img" aria-label="Boarding pictogram: house with paw print"></span>
        <span class="service__label">Boarding</span>
      </div>
      <span class="services__divider services__divider--one"></span>
      <div class="service service--daycare">
        <span class="service__icon" role="img" aria-label="Daycare pictogram: person walking a dog in the sun"></span>
        <span class="service__label">Daycare</span>
      </div>
      <span class="services__divider services__divider--two"></span>
      <div class="service service--training">
        <span class="service__icon" role="img" aria-label="Training pictogram: trainer with dog jumping through a hoop"></span>
        <span class="service__label">Training</span>
      </div>
    </div>

    <div class="contact">
      <div class="contact__phone">
        <svg width="26" height="26" viewBox="0 0 24 24" aria-hidden="true"><path fill="#fff" d="M6.6 10.8a15.1 15.1 0 0 0 6.6 6.6l2.2-2.2a1 1 0 0 1 1-.25 11.4 11.4 0 0 0 3.6.57 1 1 0 0 1 1 1V20a1 1 0 0 1-1 1A17 17 0 0 1 3 4a1 1 0 0 1 1-1h3.5a1 1 0 0 1 1 1c0 1.25.2 2.45.57 3.57a1 1 0 0 1-.25 1Z"/><path fill="none" stroke="#fff" stroke-width="1.8" stroke-linecap="round" d="M14 3.5a7 7 0 0 1 6.5 6.5M14 7a3.5 3.5 0 0 1 3 3"/></svg>
        <span>905-555-0142</span>
      </div>
      <div class="contact__web">
        <svg width="16" height="16" viewBox="0 0 16 16" aria-hidden="true"><circle cx="8" cy="8" r="6.5" fill="none" stroke="#fff" stroke-width="1.3"/><path d="M1.5 8h13M8 1.5c-3 3.5-3 9.5 0 13M8 1.5c3 3.5 3 9.5 0 13" fill="none" stroke="#fff" stroke-width="1"/></svg>
        <span>www.<strong>tailwindfields</strong>.ca</span>
      </div>
    </div>
  </section>

  <!-- Sign two: campus location -->
  <section class="sign sign--campus">
    <svg class="sign__shapes" viewBox="0 0 665 1327" preserveAspectRatio="none" aria-hidden="true">
      <path class="band-dark" d="M0,525 Q330,760 665,525 L665,610 Q380,800 0,540 Z"/>
      <path class="band-teal" d="M0,552 Q380,812 665,620 L665,1183 L0,1183 Z"/>
      <rect class="band-dark" x="0" y="1191" width="665" height="136"/>
    </svg>

    <h1 class="brand-name">TAILWIND<br>FIELDS</h1>

    <h2 class="headline headline--campus">North<br>Cedarbrook<br>Campus</h2>

    <span class="rule"></span>

    <p class="tagline">
      <span class="tagline__lead">HOME TO THE</span>
      <span class="tagline__main">SOCIAL CLUB</span>
    </p>

    <div class="contact">
      <div class="contact__phone">
        <svg width="26" height="26" viewBox="0 0 24 24" aria-hidden="true"><path fill="#fff" d="M6.6 10.8a15.1 15.1 0 0 0 6.6 6.6l2.2-2.2a1 1 0 0 1 1-.25 11.4 11.4 0 0 0 3.6.57 1 1 0 0 1 1 1V20a1 1 0 0 1-1 1A17 17 0 0 1 3 4a1 1 0 0 1 1-1h3.5a1 1 0 0 1 1 1c0 1.25.2 2.45.57 3.57a1 1 0 0 1-.25 1Z"/><path fill="none" stroke="#fff" stroke-width="1.8" stroke-linecap="round" d="M14 3.5a7 7 0 0 1 6.5 6.5M14 7a3.5 3.5 0 0 1 3 3"/></svg>
        <span>905-555-0142</span>
      </div>
      <div class="contact__web">
        <svg width="16" height="16" viewBox="0 0 16 16" aria-hidden="true"><circle cx="8" cy="8" r="6.5" fill="none" stroke="#fff" stroke-width="1.3"/><path d="M1.5 8h13M8 1.5c-3 3.5-3 9.5 0 13M8 1.5c3 3.5 3 9.5 0 13" fill="none" stroke="#fff" stroke-width="1"/></svg>
        <span>www.<strong>tailwindfields</strong>.ca</span>
      </div>
    </div>
  </section>

</body>
</html>
```